ALL TEXT GRAPHICS TM May 2025 for Instagram

We are looking for a series of social media graphics for Instagram (new size: 4:5 (1080 x 1350 pixels) ratio that are ALL TEXT. We want the following quotes below on each graphic; one quote per graphic. AND, In very small letters at the bottom of each graphic, add @TovaMarshOnline
The look and feel of these graphics should be complimentary to the color palette attached below; but keep them simple. But the design is up to you; at the end of this document, I provided various samples of all text graphics that I like as examples.
Target Market(s)
women looking to lose weight
Look and feel

```html
<!DOCTYPE html>
<html lang="en">
<head>
<meta charset="utf-8">
<title>All-Text Instagram Graphics – TM</title>
<link href="https://fonts.googleapis.com/css2?family=Bebas+Neue&family=Barlow+Condensed:wght@400;600&family=Open+Sans:wght@700&display=swap" rel="stylesheet">
<style>
  :root {
    --canvas: #ebebeb;
    --magenta: #d0026a;
    --hot-pink: #ff3399;
    --white: #ffffff;
    --ink: #2a2a2a;
  }
  * { box-sizing: border-box; margin: 0; padding: 0; }
  html, body { width: 1080px; height: 1200px; overflow: hidden; }
  body { background: var(--canvas); }

  .series {
    display: grid;
    grid-template-columns: repeat(3, 259px);
    grid-template-rows: repeat(3, 324px);
    column-gap: 72px;
    row-gap: 48px;
    padding: 66px 0 0 79px;
  }

  .card { position: relative; overflow: hidden; }
  .frame { position: absolute; }

  .message {
    position: absolute;
    left: 0; right: 0;
    text-align: center;
  }
  .headline {
    font-family: "Bebas Neue", Impact, sans-serif;
    font-weight: 400;
    font-size: 50px;
    line-height: 47px;
    letter-spacing: 0.5px;
  }
  .headline span { display: inline-block; }
  .body-copy {
    margin-top: 12px;
    font-family: "Barlow Condensed", "Arial Narrow", sans-serif;
    font-weight: 400;
    font-size: 15.5px;
    line-height: 17.5px;
    letter-spacing: 0.6px;
    text-transform: uppercase;
  }
  .body-copy .emphasis {
    display: block;
    font-weight: 600;
    font-size: 18px;
    line-height: 20px;
    letter-spacing: 0.8px;
  }
  .body-copy .emphasis.lead { margin-bottom: 0; }

  .handle {
    position: absolute;
    left: 50%;
    transform: translateX(-50%);
    font-family: "Open Sans", Arial, sans-serif;
    font-weight: 700;
    font-size: 10.5px;
    white-space: nowrap;
  }

  /* Solid magenta cards */
  .solid { background: var(--magenta); color: var(--white); }
  .solid .frame { left: 29px; top: 24px; width: 201px; height: 275px; border: 2px solid var(--white); }
  .solid .message { top: 18px; }
  .solid .headline span.break-line { background: var(--magenta); padding: 0 8px; }
  .solid .handle { top: 289px; background: var(--magenta); padding: 0 7px; line-height: 18px; color: var(--white); }

  /* White cards with magenta outline */
  .outline { background: var(--white); color: var(--ink); }
  .outline .frame { left: 29px; top: 25px; width: 201px; height: 274px; border: 2px solid var(--magenta); }
  .outline .message { top: 38px; }
  .outline .emphasis { color: var(--magenta); }
  .outline .handle { top: 289px; width: 82px; height: 16px; line-height: 16px; text-align: center; background: var(--magenta); color: var(--white); font-size: 8px; }

  /* White panel on hot-pink border */
  .framed { background: var(--hot-pink); color: var(--ink); }
  .framed .frame { left: 19px; top: 19.5px; width: 221px; height: 278px; background: var(--white); }
  .framed .message { top: 36px; }
  .framed .emphasis { color: var(--magenta); }
  .framed .handle { top: 289px; width: 82px; height: 16px; line-height: 16px; text-align: center; background: var(--magenta); color: var(--white); font-size: 8px; }

  .tight { margin-top: 8px; }
</style>
</head>
<body>
<main class="series">

  <!-- Row 1 -->
  <article class="card solid">
    <div class="frame"></div>
    <div class="message">
      <h2 class="headline"><span class="break-line">Tired.</span><br>Moody.<br>Stubborn<br>Belly Fat.</h2>
      <p class="body-copy tight">Your hormones are<br>screaming for help!<span class="emphasis">Let’s fix that.</span></p>
    </div>
    <p class="handle">@TovaMarshOnline</p>
  </article>

  <article class="card solid">
    <div class="frame"></div>
    <div class="message">
      <h2 class="headline"><span class="break-line">That</span><br>Stubborn<br>Weight?</h2>
      <p class="body-copy">It’s not your fault.<br>Your hormones are to<br>blame and you’re not alone;<span class="emphasis">But there is a fix.</span></p>
    </div>
    <p class="handle">@TovaMarshOnline</p>
  </article>

  <article class="card solid">
    <div class="frame"></div>
    <div class="message">
      <h2 class="headline"><span class="break-line">Flat</span><br>Tummy in<br>Your 40s?</h2>
      <p class="body-copy"><span class="emphasis lead">It’s still possible!</span>Comment bye belly to<br>get the 10 secrets to a<br>flatter tummy</p>
    </div>
    <p class="handle">@TovaMarshOnline</p>
  </article>

  <!-- Row 2 -->
  <article class="card outline">
    <div class="frame"></div>
    <div class="message">
      <h2 class="headline">Tired.<br>Moody.<br>Stubborn<br>Belly Fat.</h2>
      <p class="body-copy tight">Your hormones are<br>screaming for help!<span class="emphasis">Let’s fix that.</span></p>
    </div>
    <p class="handle">@TovaMarshOnline</p>
  </article>

  <article class="card outline">
    <div class="frame"></div>
    <div class="message">
      <h2 class="headline">That<br>Stubborn<br>Weight?</h2>
      <p class="body-copy">It’s not your fault.<br>Your hormones are to<br>blame and you’re not alone;<span class="emphasis">But there is a fix.</span></p>
    </div>
    <p class="handle">@TovaMarshOnline</p>
  </article>

  <article class="card outline">
    <div class="frame"></div>
    <div class="message">
      <h2 class="headline">Flat<br>Tummy in<br>Your 40s?</h2>
      <p class="body-copy"><span class="emphasis lead">It’s still possible!</span>Comment bye belly to<br>get the 10 secrets to a<br>flatter tummy</p>
    </div>
    <p class="handle">@TovaMarshOnline</p>
  </article>

  <!-- Row 3 -->
  <article class="card framed">
    <div class="frame"></div>
    <div class="message">
      <h2 class="headline">Tired.<br>Moody.<br>Stubborn<br>Belly Fat.</h2>
      <p class="body-copy tight">Your hormones are<br>screaming for help!<span class="emphasis">Let’s fix that.</span></p>
    </div>
    <p class="handle">@TovaMarshOnline</p>
  </article>

  <article class="card framed">
    <div class="frame"></div>
    <div class="message">
      <h2 class="headline">That<br>Stubborn<br>Weight?</h2>
      <p class="body-copy">It’s not your fault.<br>Your hormones are to<br>blame and you’re not alone;<span class="emphasis">But there is a fix.</span></p>
    </div>
    <p class="handle">@TovaMarshOnline</p>
  </article>

  <article class="card framed">
    <div class="frame"></div>
    <div class="message">
      <h2 class="headline">Flat<br>Tummy in<br>Your 40s?</h2>
      <p class="body-copy"><span class="emphasis lead">It’s still possible!</span>Comment bye belly to<br>get the 10 secrets to a<br>flatter tummy</p>
    </div>
    <p class="handle">@TovaMarshOnline</p>
  </article>

</main>
</body>
</html>
```